Website Pravelo Research Solutions

We are a small European high-tech online research company.
With our own state of the art software we run online panels and are conducting reseach for companies. Partly research via our own panel and partly via panels we maintain for our customers.
Our current website is old and outdatet: www.pravelo.nl.
We are in the process to change the content of the site. We want a modern, european and businesslike design for our new website.
Our logo has to stay the same (left uppersite of our website and attached) but can be changed a little to adapt it to the new design of the website. The colors of the site are up to you.
Target Market(s)
Marketeers and researchers of large and middle size companies in all kind of fields.
Industry/Entity Type
Online
Look and feel
Each slider illustrates characteristics of the customer's brand and the style your logo design should communicate.

```html
<!DOCTYPE html>
<html lang="nl">
<head>
<meta charset="utf-8">
<title>Pravelo Research Solutions</title>
<link rel="stylesheet" href="https://fonts.googleapis.com/css2?family=Roboto+Condensed:wght@400;700&family=PT+Sans:wght@400;700&family=Arimo:wght@400;700&display=swap">
<style>
  :root {
    --page-bg: #e4e4e4;
    --sheet: #ffffff;
    --brand-blue: #2d5a9a;
    --welcome-blue: #3a6aaa;
    --hero-dark: #1b4a92;
    --hero-light: #4a82cc;
    --bar-blue: #1f4f94;
    --accent-yellow: #f6c94a;
    --text-grey: #666666;
    --nav-text: #333333;
    --soft-grey: #9a9a9a;
    --note-top: #fff9d6;
    --note-bottom: #fdf0a6;
    --note-border: #f1df8f;
    --field-border: #cfcfcf;
    --submit: #1c2f8a;
  }
  * { box-sizing: border-box; margin: 0; padding: 0; }
  html, body { width: 1189px; height: 1200px; overflow: hidden; }
  body { background: var(--page-bg); font-family: "Arimo", Arial, sans-serif; position: relative; }
  .sheet { position: absolute; left: 63px; top: 0; width: 1066px; height: 1200px; background: var(--sheet); box-shadow: 0 0 4px rgba(0,0,0,.15); }
  .abs { position: absolute; }

  /* header */
  .brand { left: 100px; top: 46px; display: flex; align-items: center; gap: 14px; }
  .brand-dot { width: 34px; height: 34px; border-radius: 50%; background: var(--brand-blue); }
  .brand-name { font-family: "PT Sans", sans-serif; font-weight: 700; font-size: 36px; color: var(--brand-blue); }
  .social-row { left: 978px; top: 14px; display: flex; gap: 8px; align-items: center; }
  .social-chip { width: 22px; height: 22px; border-radius: 4px; background: #c9d5e6; }
  .phone { left: 881px; top: 78px; display: flex; align-items: center; gap: 6px; font-family: "PT Sans", sans-serif; font-size: 22px; color: var(--soft-grey); }

  /* nav */
  .main-nav { left: 63px; top: 128px; width: 1066px; height: 51px; background: linear-gradient(#dcdee2, #f7f7f7 45%, #ececec); }
  .main-nav a { position: absolute; top: 14px; transform: translateX(-50%); font-family: "Roboto Condensed", sans-serif; font-weight: 700; font-size: 19px; color: var(--nav-text); text-decoration: none; letter-spacing: .6px; }

  /* hero */
  .hero { left: 63px; top: 179px; width: 1066px; height: 305px; background: linear-gradient(100deg, var(--hero-dark), #2f64b0 45%, var(--hero-light)); overflow: hidden; }
  .hero-photo { position: absolute; left: 553px; top: 0; width: 513px; height: 305px; background: linear-gradient(90deg, rgba(110,140,190,0), #b9c2cf 40%, #e4e6ea); }
  .hero-title { position: absolute; left: 81px; top: 40px; font-family: "Roboto Condensed", sans-serif; font-weight: 700; font-size: 52px; line-height: 1; color: #fff; }
  .hero-sub { position: absolute; left: 81px; top: 86px; font-family: "Roboto Condensed", sans-serif; font-weight: 700; font-size: 22px; color: var(--accent-yellow); }
  .hero-bar { position: absolute; left: 76px; width: 390px; height: 40px; background: linear-gradient(#2a5ca6, var(--bar-blue)); border: 1px solid #3c6db5; box-shadow: 0 1px 3px rgba(0,0,0,.3); color: #fff; font-family: "Roboto Condensed", sans-serif; font-weight: 700; font-size: 13.5px; padding: 10px 0 0 19px; }
  .hero-bar svg { position: absolute; right: 12px; top: 16px; }

  /* welcome */
  .welcome { left: 90px; top: 508px; width: 494px; }
  .welcome h1 { font-family: "PT Sans", sans-serif; font-weight: 700; font-size: 34px; color: var(--welcome-blue); margin-bottom: 2px; }
  .welcome p { font-size: 15.5px; line-height: 28px; color: var(--text-grey); text-align: justify; hyphens: auto; }
  .gap { height: 28px; }

  /* note */
  .note { left: 604px; top: 500px; width: 256px; height: 485px; border: 1px solid var(--note-border); border-radius: 10px; background: linear-gradient(var(--note-top), var(--note-bottom)); padding: 14px 14px 0 19px; }
  .note h2 { font-family: "PT Sans", sans-serif; font-weight: 700; font-size: 26px; color: #111; margin-bottom: 6px; }
  .note p { font-size: 15.5px; line-height: 28px; color: #111; padding-left: 4px; }

  /* demo */
  .demo { left: 877px; top: 503px; width: 225px; height: 195px; }
  .demo-screen { width: 225px; height: 159px; background: radial-gradient(circle at 50% 40%, #4a4a4a, #262626 75%); position: relative; }
  .demo-screen span { position: absolute; left: 0; right: 0; top: 118px; text-align: center; font-family: "Roboto Condensed", sans-serif; font-weight: 700; font-size: 20px; color: #fff; }
  .demo-controls { height: 36px; background: linear-gradient(#e6e6e6, #b5b5b5); position: relative; }

  /* form */
  .enquiry { left: 873px; top: 717px; width: 231px; height: 268px; background: linear-gradient(90deg, #f4f4f4, #e3e3e3 50%, #f0f0f0); padding: 10px 17px; }
  .enquiry h3 { font-weight: 400; font-size: 17px; color: #111; margin: 0 0 12px -2px; }
  .field { width: 197px; height: 28px; border: 1px solid var(--field-border); background: #fff; font-size: 12.5px; color: #888; padding: 5px 11px; margin-bottom: 4px; letter-spacing: .4px; }
  .field.area { height: 71px; }
  .submit { position: absolute; left: 135px; top: 226px; width: 79px; height: 30px; border-radius: 9px; background: linear-gradient(#2c45a8, var(--submit)); color: #fff; font-weight: 700; font-size: 15px; text-align: center; line-height: 30px; }

  /* footer */
  .footer-nav { left: 95px; top: 1009px; width: 1000px; height: 53px; background: linear-gradient(#fff, #f6f6f6 50%, #fff); border-top: 1px solid #eee; border-bottom: 1px solid #e6e6e6; }
  .footer-nav a { position: absolute; top: 16px; transform: translateX(-50%); font-size: 16px; color: #777; text-decoration: none; }
  .footer-brand { left: 92px; top: 1103px; display: flex; align-items: center; gap: 5px; }
  .footer-brand .dot { width: 18px; height: 18px; border-radius: 50%; background: #c8c8c8; }
  .footer-brand span { font-family: "PT Sans", sans-serif; font-weight: 700; font-size: 16px; color: #bdbdbd; }
  .legal { left: 187px; top: 1099px; font-size: 11.5px; line-height: 19px; color: #444; }
</style>
</head>
<body>
<div class="sheet"></div>

<header>
  <div class="abs brand"><div class="brand-dot"></div><span class="brand-name">Pravelo Research Solutions</span></div>
  <div class="abs social-row">
    <div class="social-chip"></div><div class="social-chip"></div><div class="social-chip"></div>
    <svg width="30" height="20" viewBox="0 0 30 20" aria-label="E-mail"><rect x="1" y="1" width="28" height="18" rx="2" fill="#eee" stroke="#bbb"/><path d="M1 2 L15 12 L29 2" fill="none" stroke="#aaa" stroke-width="1.5"/></svg>
  </div>
  <div class="abs phone">
    <svg width="28" height="34" viewBox="0 0 28 34" aria-hidden="true"><path d="M6 2 C2 4 1 10 5 18 C9 26 15 31 21 32 L25 26 L19 21 L15 24 C12 21 10 17 9 13 L13 11 L11 3 Z" fill="#b5b5b5"/></svg>
    +31 (0)20 555 0142
  </div>
</header>

<nav class="abs main-nav">
  <a style="left:83px">ALGEMEEN</a>
  <a style="left:243px">PRODUCTEN</a>
  <a style="left:392px">DEMO'S</a>
  <a style="left:516px">MEDIA</a>
  <a style="left:662px">REFERENTIES</a>
  <a style="left:830px">PERSONEEL</a>
  <a style="left:980px">CONTACT</a>
</nav>

<section class="abs hero">
  <div class="hero-photo" role="img" aria-label="Foto van een team collega's dat lachend samen naar een computerscherm kijkt"></div>
  <div class="hero-title">STABILITY</div>
  <div class="hero-sub">&amp; EMPHASIS ON CLIENT ADVOCACY</div>
  <div class="hero-bar" style="top:127px">Lorem ipsum dolor sit amet, consectetur adipiscing elit.<svg width="6" height="8"><path d="M0 0L6 4L0 8Z" fill="#fff"/></svg></div>
  <div class="hero-bar" style="top:174px">Lorem ipsum dolor sit amet, consectetur adipiscing elit.<svg width="6" height="8"><path d="M0 0L6 4L0 8Z" fill="#fff"/></svg></div>
  <div class="hero-bar" style="top:223px">Lorem ipsum dolor sit amet, consectetur adipiscing elit.<svg width="6" height="8"><path d="M0 0L6 4L0 8Z" fill="#fff"/></svg></div>
</section>

<main>
  <article class="abs welcome">
    <h1>Welcome</h1>
    <p>Pravelo is gespecialiseerd in online gegevensverzameling en analyse en is werkzaam voor internationale opdrachtgevers.</p>
    <div class="gap"></div>
    <p>Het bedrijf werd opgericht in 1996 en is gevestigd in Veldhaven, een kleine havenplaats boven Zaanhaven. Onze produkten zijn ontwikkeld op basis van Qvest, een krachtige en uitermate flexibele onderzoekstool voor het verzamelen &amp; verwerken van (online) researchgegevens.</p>
    <p>Qvest werd ontwikkeld dóór opinieonderzoekers vóór opinieonder&shy;zoekers.</p>
    <div class="gap"></div>
    <p>Ons team bestaat uit zowel opinieonderzoekers als programmeurs met vele jaren ervaring op het gebied van opinieonderzoek en met name met online toepassingen daarvoor.</p>
  </article>

  <aside class="abs note">
    <h2>Dataverzameling</h2>
    <p>Pravelo is uitgegroeid tot een volwaardig speler in de markt met een indrukwekkend(e) portfolio. Zo heeft Pravelo sinds haar oprichting wereld-wijd meer dan 2.000.000 vragenlijsten afgenomen in diverse talen en voor diverse opdrachtgevers. Onze dienst-verlening beperkt zich tot het verzamelen van data, Pravelo trekt geen conclusies maar stelt haar klanten middels ons online ...</p>
  </aside>

  <div class="abs demo">
    <div class="demo-screen">
      <svg style="position:absolute;left:92px;top:52px" width="44" height="52" viewBox="0 0 44 52" aria-hidden="true"><path d="M0 0L44 26L0 52Z" fill="#fff"/></svg>
      <span>Check Out the Demo</span>
    </div>
    <div class="demo-controls">
      <svg width="225" height="36" viewBox="0 0 225 36" aria-hidden="true">
        <rect x="7" y="6" width="25" height="24" fill="#6a6a9a"/>
        <rect x="79" y="6" width="68" height="24" rx="12" fill="#dcdcdc" stroke="#999"/>
        <circle cx="113" cy="18" r="5" fill="#b04040"/>
        <rect x="174" y="9" width="11" height="8" rx="1" fill="#444"/>
        <rect x="196" y="9" width="10" height="8" fill="#444"/><path d="M206 13L212 9V17Z" fill="#444"/>
        <rect x="174" y="21" width="40" height="9" rx="4.5" fill="#fff" stroke="#888"/><circle cx="209" cy="25.5" r="4" fill="#888"/>
      </svg>
    </div>
  </div>

  <form class="abs enquiry">
    <h3>Enquiry form</h3>
    <div class="field">Name :</div>
    <div class="field">Email :</div>
    <div class="field">Phone :</div>
    <div class="field area">Comments:</div>
    <div class="submit">Submit</div>
  </form>
</main>

<footer>
  <nav class="abs footer-nav">
    <a style="left:130px">Algemeen</a>
    <a style="left:263px">Producten</a>
    <a style="left:381px">Demo's</a>
    <a style="left:483px">Media</a>
    <a style="left:607px">Referenties</a>
    <a style="left:743px">Personeel</a>
    <a style="left:866px">Contact</a>
  </nav>
  <div class="abs footer-brand"><div class="dot"></div><span>Pravelo</span></div>
  <div class="abs legal">Copyright (C) 2010 Pravelo Research Solutions. All Rights Reserved.<br>Privacy Policy | Sitemap</div>
</footer>
</body>
</html>
```